Security Guard Company Postcard

I am looking for a postcard to be created so I can send to potential clients for sales and marketing purposes for my security guard division. NOT Investigations! I have added a photo of my logo and I am looking to have the following services included:
Permanent Security Services
Temporary Security Services
Emergency Services
Fire Watch
Alarm Response
Private Investigations
Background Checks
ALPR Camera Systems

Are just to name a few of our services. Please contact me at mdunbar@pivanco.com for any questions.
Thank you!
Marcus

Security

Security

• Any wording on Investigations

```html
<!DOCTYPE html>
<html lang="en">
<head>
<meta charset="utf-8">
<title>Pivanco Security Postcard</title>
<link href="https://fonts.googleapis.com/css2?family=Archivo+Black&family=Oswald:wght@300;400&family=Roboto+Condensed:wght@700&family=Open+Sans:wght@400&display=swap" rel="stylesheet">
<style>
  :root {
    --page-bg: #e6e6e6;
    --card-dark: #333333;
    --card-darker: #262626;
    --photo-light: #6a6a6a;
    --photo-dark: #2c2c2c;
    --accent-blue: #2a9bd8;
    --accent-tan: #c49a6c;
    --white: #ffffff;
    --ink: #1e1e1e;
    --rule: #9a9a9a;
  }
  * { margin: 0; padding: 0; box-sizing: border-box; }
  html, body { width: 1189px; height: 1200px; overflow: hidden; }
  body { background: var(--page-bg); position: relative; }

  .postcard {
    position: absolute;
    left: 281px;
    width: 658px;
    height: 421px;
    overflow: hidden;
    box-shadow: 0 3px 10px rgba(0,0,0,.25);
  }
  .postcard--front {
    top: 112px;
    background: linear-gradient(120deg, var(--card-dark), var(--card-darker));
  }
  .postcard--back {
    top: 568px;
    background: var(--white);
    border: 1px solid #bdbdbd;
  }

  .uniform-photo {
    position: absolute; left: 0; top: 0; width: 390px; height: 421px;
    background: radial-gradient(ellipse at 45% 40%, var(--photo-light), var(--photo-dark) 75%);
    -webkit-mask-image: linear-gradient(90deg, #000 70%, transparent);
            mask-image: linear-gradient(90deg, #000 70%, transparent);
  }

  .brand-name {
    position: absolute;
    font-family: "Archivo Black", sans-serif;
    font-size: 40px;
    line-height: 1;
    letter-spacing: 0.5px;
  }
  .brand-name--front { left: 32px; top: 56px; color: var(--accent-tan); }
  .brand-name--back { left: 22px; top: 248px; color: var(--ink); }

  .call-block { position: absolute; left: 30px; top: 330px; }
  .call-icon { position: absolute; left: 0; top: 2px; }
  .call-label {
    position: absolute; left: 48px; top: 0; white-space: nowrap;
    font-family: "Oswald", sans-serif; font-weight: 300; font-size: 17px; color: var(--white);
  }
  .call-number {
    position: absolute; left: 48px; top: 22px; white-space: nowrap;
    font-family: "Oswald", sans-serif; font-weight: 400; font-size: 28px; color: var(--white);
    letter-spacing: -0.5px;
  }

  .service-list { position: absolute; left: 330px; top: 51px; list-style: none; }
  .service-item {
    display: flex; align-items: center; height: 43.5px;
    font-family: "Roboto Condensed", sans-serif; font-weight: 700; font-size: 22px; color: var(--white);
    white-space: nowrap;
  }
  .service-marker {
    width: 18px; height: 18px; border-radius: 50%;
    background: var(--accent-blue); margin-right: 22px; flex: none;
  }

  .stamp-box {
    position: absolute; left: 512px; top: 25px; width: 73px; height: 86px;
    border: 1px solid #8c8c8c;
  }
  .address-line {
    position: absolute; left: 336px; width: 249px; height: 0;
    border-top: 1px dotted var(--rule);
  }

  .contact-list { position: absolute; left: 57px; top: 318px; list-style: none; }
  .contact-item {
    display: flex; align-items: flex-start; min-height: 14px;
    font-family: "Open Sans", sans-serif; font-size: 11px; line-height: 14px; color: var(--ink);
  }
  .contact-icon { width: 13px; height: 13px; margin-right: 3px; flex: none; }
  .contact-text--indent { padding-left: 16px; }
</style>
</head>
<body>

  <section class="postcard postcard--front">
    <div class="uniform-photo" role="img" aria-label="Photo of a security guard in a dark uniform with arms crossed"></div>

    <div class="brand-name brand-name--front">PIVANCO</div>

    <div class="call-block">
      <svg class="call-icon" width="36" height="42" viewBox="0 0 36 42" aria-hidden="true">
        <path d="M6 3 L13 1 L17 12 L12 15 C14 23 18 29 24 33 L28 29 L35 36 L31 41 C18 40 6 26 3 10 Z"
              fill="none" stroke="#2a9bd8" stroke-width="2.4" stroke-linejoin="round"/>
      </svg>
      <div class="call-label">CALL US TODAY</div>
      <div class="call-number">00 54&nbsp; 9 210 4408317</div>
    </div>

    <ul class="service-list">
      <li class="service-item"><span class="service-marker"></span>Permanent Security Services</li>
      <li class="service-item"><span class="service-marker"></span>Temporary Security Services</li>
      <li class="service-item"><span class="service-marker"></span>Emergency Services</li>
      <li class="service-item"><span class="service-marker"></span>Fire Watch</li>
      <li class="service-item"><span class="service-marker"></span>Alarm Response</li>
      <li class="service-item"><span class="service-marker"></span>Private Investigations</li>
      <li class="service-item"><span class="service-marker"></span>Background Checks</li>
      <li class="service-item"><span class="service-marker"></span>ALPR Camera Systems</li>
    </ul>
  </section>

  <section class="postcard postcard--back">
    <div class="stamp-box"></div>
    <div class="address-line" style="top:168px"></div>
    <div class="address-line" style="top:226px"></div>
    <div class="address-line" style="top:261px"></div>

    <div class="brand-name brand-name--back">PIVANCO</div>

    <ul class="contact-list">
      <li class="contact-item">
        <svg class="contact-icon" viewBox="0 0 14 14" aria-hidden="true"><path d="M7 1 L13 7 H11 V13 H8.5 V9 H5.5 V13 H3 V7 H1 Z" fill="#1e1e1e"/></svg>
        <span>Harbor Meeting Hall</span>
      </li>
      <li class="contact-item"><span class="contact-text--indent">18-Alder Road Westbrook Heights</span></li>
      <li class="contact-item">
        <svg class="contact-icon" viewBox="0 0 14 14" aria-hidden="true"><path d="M11 1 L13 3 L11 6 L9.5 5 C8.5 7 7 8.5 5 9.5 L6 11 L3 13 L1 11 C2 6 6 2 11 1 Z" fill="#1e1e1e"/></svg>
        <span>555-204-7719</span>
      </li>
      <li class="contact-item">
        <svg class="contact-icon" viewBox="0 0 14 14" aria-hidden="true"><circle cx="7" cy="7" r="2.6" fill="none" stroke="#1e1e1e" stroke-width="1.4"/><path d="M9.6 5 V8.3 C9.6 10 12.6 10 12.6 7 A5.6 5.6 0 1 0 10 11.8" fill="none" stroke="#1e1e1e" stroke-width="1.4"/></svg>
        <span>PivancoGuard</span>
      </li>
    </ul>
  </section>

</body>
</html>
```